Business cards Marta Keller Sport & Events

I need new business cards to match my new logo design for my company called "Marta Keller Sport & Events". I'm based in Germany.
With my company, I offer different services in the context of sport.

Marta Keller owner

Marta Keller Sports & Events
Birkendorfer Weg 14
D-63158 Offenbach

+49 69 / 31 52 94 07
info@marta-keller-sport.example
www.marta-keller-sport.example

Contact Information for Business Card

Marta Keller Inhaberin Marta Keller Sport & Events Birkendorfer Weg 14 D-63158 Offenbach +49 69 / 31 52 94 07 info@marta-keller-sport.example www.marta-keller-sport.example

Requirements
Must have
• Logo | Double sided business card

```html
<!DOCTYPE html>
<html lang="de">
<head>
<meta charset="utf-8">
<title>Marta Keller Sport &amp; Events – Visitenkarten</title>
<link rel="stylesheet" href="https://fonts.googleapis.com/css2?family=Arimo:wght@400;700&display=swap">
<style>
  :root {
    --backdrop: #e4e4e2;
    --card-dark: #2a2a2c;
    --card-dark-soft: #323235;
    --accent: #f0a01e;
    --ink-light: #f4f4f4;
    --ink-muted: #d8d8d8;
  }
  * { box-sizing: border-box; margin: 0; padding: 0; }
  html, body { width: 1200px; height: 801px; overflow: hidden; }
  body {
    background: var(--backdrop);
    font-family: "Arimo", Arial, sans-serif;
    position: relative;
  }
  .card {
    position: absolute;
    top: 245px;
    width: 540px;
    height: 310px;
    background: var(--card-dark);
    overflow: hidden;
    box-shadow: 0 10px 24px rgba(0,0,0,0.18);
  }
  .card--front { left: 40px; }
  .card--back { left: 620px; }

  /* front */
  .front-band {
    position: absolute; left: 0; right: 0; bottom: 0; height: 10px;
    background: var(--accent);
  }
  .brand {
    position: absolute; display: flex; align-items: center; gap: 12px;
  }
  .brand__dot {
    width: 54px; height: 54px; border-radius: 50%;
    background: var(--accent); flex: none;
  }
  .brand__name {
    color: var(--ink-light); font-weight: 700; text-transform: uppercase;
    line-height: 1.15; letter-spacing: 1px;
  }
  .card--front .brand { left: 32px; top: 32px; }
  .card--front .brand__name { font-size: 17px; width: 220px; }

  .holder { position: absolute; left: 32px; top: 128px; }
  .holder__name {
    color: var(--accent); font-weight: 700; font-size: 24px;
    text-transform: uppercase; letter-spacing: 0.5px;
  }
  .holder__role { color: var(--ink-light); font-size: 15px; margin-top: 4px; }

  .contact { position: absolute; left: 32px; top: 205px; list-style: none; }
  .contact li {
    display: flex; align-items: center; gap: 10px;
    color: var(--ink-light); font-size: 14px; line-height: 24px;
  }
  .contact svg { width: 15px; height: 15px; fill: var(--accent); flex: none; }

  .address {
    position: absolute; right: 30px; top: 40px; text-align: right;
    color: var(--ink-light); font-size: 14px; line-height: 1.55;
    font-style: normal;
  }

  /* back */
  .back-texture {
    position: absolute; inset: 0;
    background: radial-gradient(ellipse at 50% 45%, #353538 0%, var(--card-dark) 70%);
  }
  .back-edge {
    position: absolute; left: 0; right: 0; bottom: 0; height: 4px;
    background: var(--accent);
  }
  .card--back .brand {
    left: 50%; top: 50%; transform: translate(-50%, -50%);
    flex-direction: column; text-align: center; gap: 14px;
  }
  .card--back .brand__dot { width: 62px; height: 62px; }
  .card--back .brand__name { font-size: 20px; letter-spacing: 2px; }
</style>
</head>
<body>

<section class="card card--front" aria-label="Vorderseite">
  <div class="brand">
    <span class="brand__dot"></span>
    <span class="brand__name">Marta Keller Sport &amp; Events</span>
  </div>

  <address class="address">
    Birkendorfer<br>Weg 14<br>D-63158 Offenbach
  </address>

  <div class="holder">
    <p class="holder__name">Marta Keller</p>
    <p class="holder__role">Inhaberin</p>
  </div>

  <ul class="contact">
    <li>
      <svg viewBox="0 0 16 16" aria-hidden="true"><path d="M3.2 1.5l2.3 0 1.1 3.2-1.6 1.2c.8 1.8 2.2 3.2 4 4l1.2-1.6 3.2 1.1v2.3c0 .9-.8 1.6-1.7 1.5C6.4 12.7 3.3 9.6 2.8 4.1 2.7 2.2 2.3 1.5 3.2 1.5z"/></svg>
      +49 69 / 31 52 94 07
    </li>
    <li>
      <svg viewBox="0 0 16 16" aria-hidden="true"><path d="M1 3h14v10H1z M2.5 4.5v.4L8 8.8l5.5-3.9v-.4z" fill-rule="evenodd"/></svg>
      info@marta-keller-sport.example
    </li>
    <li>
      <svg viewBox="0 0 16 16" aria-hidden="true"><path d="M8 1a7 7 0 1 0 0 14A7 7 0 0 0 8 1zm0 2.2L10.4 5 9.5 7.8h-3L5.6 5zM3 8.6l1.9-.6 1 2.9-1.3 1.9A5 5 0 0 1 3 8.6zm8.4 4.2-1.3-1.9 1-2.9 1.9.6a5 5 0 0 1-1.6 4.2z"/></svg>
      www.marta-keller-sport.example
    </li>
  </ul>

  <div class="front-band"></div>
</section>

<section class="card card--back" aria-label="Rückseite">
  <div class="back-texture" role="img" aria-label="Dunkle Prägefläche mit wiederholtem Markenmuster"></div>
  <div class="brand">
    <span class="brand__dot"></span>
    <span class="brand__name">Marta Keller<br>Sport &amp; Events</span>
  </div>
  <div class="back-edge"></div>
</section>

</body>
</html>
```